Etiketten für junge Imkerei
Zielgruppe
Wir sind eine junge Imkerei, die spezielle und außergewöhnliche Honigspezialitäten vermarktet.
Ich verkaufe meine Produkte hauptsächlich auf dem Markt im direkten Kundenkontakt, dennoch wird ein Barcode benötigt da einige Produkte auch im Laden verfügbar sind. Meine Kunden sind hauptsächlich Frauen im mittleren Alter.
Heute brauche ich Etiketten für meine neuen OXYMEL (Sauerhonig) Produkte, Oxymel ist ein Arzneisaft der bereits in der Antike verwendet wurde:
- Amber Meadow (Blütenhonig, Apfelessig, Zitrone, Ingwer und Kurkuma)
- Storm Tonic (Apfelessig, Blütenhonig, Zwiebel, Ingwer, Meerrettich, Knoblauch, Senf, Zimt, Gewürznelken, Chilli, Blutorange)
- Kids (Blütenhonig, Apfelessig, Hagebutte, Holunderblüte)
Aufgabenstellung
Es soll ein Flaschenetikett werden.
Die Etikettengröße soll ungefähr 40x120 mm sein, wobei ich hier nicht auf eine genaue Rechteckige Form festgelegt bin, sondern auch gerne eine freie Form (z.B. Logo außerhalb). Dann bis max. 60mm hoch. Ich verwende die Flasche Bergen von Flaconia.
Inhalt: 200 ml.
Verwendetes Papier: Baumwollpapier
Barcode
Das Etikett soll vom Schema zu meinen anderen Etiketten passen. Es soll feminin und ein wenig verspielt sein aber edel wirken.
Es soll die Natürlichkeit wiederspiegeln aber nicht nach Arznei aussehen.
Im Anhang befinden sich 2 von meinen aktuellen Etiketten der Honige, diese werden auf Biofolie gedruckt.

```html
<!DOCTYPE html>
<html lang="de">
<head>
<meta charset="utf-8">
<title>Oxymel Storm Tonic – Flaschenetikett</title>
<link rel="stylesheet" href="https://fonts.googleapis.com/css2?family=Baloo+2:wght@400;500;600;700;800&display=swap">
<style>
  :root {
    --paper: #ffffff;
    --frame-pink: #e2237f;
    --ink: #111111;
    --flame-red: #e9582b;
    --flame-orange: #f39a2c;
    --flame-yellow: #f8c244;
    --accent-orange: #e8892a;
    --brand-brown: #8a6a3e;
    --honey: #e9b24a;
    --barcode-green: #8ec596;
    --barcode-text: #1e2a20;
  }
  * { margin: 0; padding: 0; box-sizing: border-box; }
  html, body {
    width: 1200px;
    height: 3124px;
    overflow: hidden;
    background: var(--paper);
  }
  .label {
    position: relative;
    width: 1200px;
    height: 3124px;
    font-family: "Baloo 2", sans-serif;
    color: var(--ink);
  }
  .label-frame {
    position: absolute;
    inset: 0;
  }
  .brand-mark {
    position: absolute;
    left: 0;
    width: 1200px;
    top: 330px;
    display: flex;
    flex-direction: column;
    align-items: center;
  }
  .brand-dot {
    width: 230px;
    height: 230px;
    border-radius: 50%;
    background: var(--honey);
    opacity: .85;
  }
  .brand-name {
    margin-top: 40px;
    font-size: 78px;
    font-weight: 500;
    color: var(--brand-brown);
    letter-spacing: 2px;
    line-height: 1;
  }
  .product-type {
    position: absolute;
    top: 880px;
    left: 0;
    width: 1200px;
    text-align: center;
    font-size: 212px;
    font-weight: 800;
    letter-spacing: 4px;
    line-height: 1;
  }
  .flame-emblem {
    position: absolute;
    left: 0;
    top: 0;
  }
  .product-name {
    position: absolute;
    top: 1850px;
    left: 0;
    width: 1200px;
    text-align: center;
    font-size: 116px;
    font-weight: 600;
    letter-spacing: 3px;
    line-height: 1;
  }
  .product-name .first { color: var(--flame-red); }
  .product-name .second { color: var(--flame-orange); }
  .ingredients {
    position: absolute;
    top: 2050px;
    left: 150px;
    width: 900px;
    text-align: center;
  }
  .ingredients-title {
    font-size: 56px;
    font-weight: 700;
    color: var(--accent-orange);
    line-height: 1.1;
    margin-bottom: 6px;
  }
  .ingredients-list {
    font-size: 43px;
    font-weight: 500;
    line-height: 64px;
  }
  .volume {
    position: absolute;
    top: 2390px;
    right: 200px;
    font-size: 76px;
    font-weight: 600;
    color: var(--accent-orange);
    line-height: 1;
  }
  .barcode-area {
    position: absolute;
    left: 168px;
    top: 2528px;
    width: 840px;
    height: 324px;
    background: var(--barcode-green);
    display: flex;
    align-items: center;
    justify-content: center;
    font-size: 50px;
    font-weight: 500;
    color: var(--barcode-text);
  }
</style>
</head>
<body>
  <main class="label">
    <svg class="label-frame" width="1200" height="3124" viewBox="0 0 1200 3124" aria-hidden="true">
      <path d="M200,520 H447 A175,175 0 1 1 753,520 H992 A80,80 0 0 1 1072,600 V2820 A80,80 0 0 1 992,2900 H200 A80,80 0 0 1 120,2820 V600 A80,80 0 0 1 200,520 Z"
            fill="none" stroke="var(--frame-pink)" stroke-width="12" stroke-linejoin="round"/>
    </svg>

    <div class="brand-mark">
      <span class="brand-dot"></span>
      <span class="brand-name">Wabenliesl</span>
    </div>

    <h1 class="product-type">OXYMEL</h1>

    <svg class="flame-emblem" width="1200" height="1900" viewBox="0 0 1200 1900">
      <path d="M330,1820 A300,300 0 1 1 870,1820" fill="none" stroke="var(--flame-orange)" stroke-width="8" stroke-linecap="round"/>
      <rect role="img" aria-label="Illustration einer lodernden Flamme in Rot, Orange und Gelb"
            x="390" y="1320" width="420" height="500" rx="60"
            fill="url(#flameTones)"/>
      <defs>
        <linearGradient id="flameTones" x1="0" y1="0" x2="0" y2="1">
          <stop offset="0" stop-color="#e9582b"/>
          <stop offset=".6" stop-color="#f39a2c"/>
          <stop offset="1" stop-color="#f8c244"/>
        </linearGradient>
      </defs>
    </svg>

    <p class="product-name"><span class="first">STORM</span><span class="second">TONIC</span></p>

    <section class="ingredients">
      <h2 class="ingredients-title">Inhalt</h2>
      <p class="ingredients-list">Apfelessig, Blütenhonig, Zwiebel, Ingwer,<br>Meerrettich, Knoblauch, Senf, Zimt,<br>Gewürznelken, Chilli &amp; Blutorange</p>
    </section>

    <p class="volume">200 ml</p>

    <div class="barcode-area">Platzhalter für Barcode</div>
  </main>
</body>
</html>
```